A Free Lance Author needs a design for his new book - The Quiet Lantern Path

Project Overview:
We're seeking a new cover design for "The Quiet Lantern Path" that captures the essence of a spiritual journey. The design should feature a majestic, natural mountain landscape with climbers ascending from various sides towards a radiant light at the summit.
Key Elements:
A grand, natural mountain with trees, rocks, etc. and a warm light at the summit, symbolizing the divine or supreme goal.
Climbers (depicted in a soft, subtle manner) ascending from different sides of the mountain, conveying the idea that individuals may be on their own unique paths, yet converging towards a common destination.
Some climbers may be visible to each other, while others may be hidden from view, representing the idea that travelers may or may not be aware of others on similar journeys until they reach the summit.
The design should evoke a sense of mystery, contemplation, and connection to nature.
Design Requirements:
The title "The Quiet Lantern Path" and its location on the Cover should be prominently displayed in a clear, readable font that stands out against the background.
The subtitle and author information should be included in a font that's easy to read and complementary to the title font.
Font colors should have sufficient contrast with the background to ensure readability and visual appeal.
Consider using a combination of font sizes and styles to create visual hierarchy and emphasis.
Specific Requirements:
The only elements that can be copied from the existing design are the title, subtitle, and author information (including the various write-up's). Everything else should be new and original.
Project Context:
We have already secured a publisher, and the internal design of the book has been completed to our satisfaction.
The cover design will be delivered to the publisher once it's finalized.
Deliverables:
A high-resolution digital file of the cover design that is adaptable for both print and digital formats.
This updated description captures the essence of the climbers' journey and the themes of the book.

```html
<!DOCTYPE html>
<html lang="en">
<head>
<meta charset="utf-8">
<title>The Quiet Lantern Path — Book Cover</title>
<link rel="stylesheet" href="https://fonts.googleapis.com/css2?family=Antonio:wght@700&family=Josefin+Sans:wght@400;700&display=swap">
<style>
  :root {
    --page-bg: #e9ecef;
    --sky-violet: #4b3a8c;
    --sky-magenta: #d5479b;
    --sky-rose: #f07aa8;
    --sun-gold: #f9c872;
    --sun-core: #fff1c8;
    --ridge-teal: #5fb5bd;
    --ridge-blue: #2b6e95;
    --valley-navy: #1b4866;
    --ground-dark: #08090c;
    --title-white: #ffffff;
    --title-navy: #0f3f6b;
    --title-teal: #1cc7c4;
    --author-teal: #22c2c0;
  }
  * { margin: 0; padding: 0; box-sizing: border-box; }
  html, body {
    width: 1200px;
    height: 806px;
    overflow: hidden;
    background: var(--page-bg);
  }
  .stage {
    width: 1200px;
    height: 806px;
    display: flex;
    align-items: center;
    justify-content: center;
  }
  .cover {
    position: relative;
    width: 523px;
    height: 740px;
    overflow: hidden;
    box-shadow: 0 10px 30px rgba(0, 0, 0, 0.25);
  }
  .cover-art {
    position: absolute;
    inset: 0;
    background:
      radial-gradient(ellipse 55% 30% at 50% 40%, var(--sun-core) 0%, rgba(249, 200, 114, 0.75) 40%, rgba(249, 200, 114, 0) 100%),
      linear-gradient(180deg,
        var(--sky-violet) 0%,
        var(--sky-magenta) 18%,
        var(--sky-rose) 30%,
        var(--sun-gold) 42%,
        var(--ridge-teal) 56%,
        var(--ridge-blue) 68%,
        var(--valley-navy) 80%,
        var(--ground-dark) 100%);
  }
  .cover-text {
    position: absolute;
    inset: 0;
    text-align: center;
  }
  .title-lead {
    position: absolute;
    top: 108px;
    left: 0;
    right: 0;
    font-family: "Josefin Sans", sans-serif;
    font-weight: 700;
    font-size: 30px;
    letter-spacing: 0.2em;
    color: var(--title-white);
  }
  .title-main {
    position: absolute;
    top: 150px;
    left: 0;
    right: 0;
    font-family: "Antonio", sans-serif;
    font-weight: 700;
    font-size: 196px;
    line-height: 1;
    letter-spacing: 0.02em;
    background: linear-gradient(90deg, var(--title-navy) 20%, var(--title-teal) 95%);
    -webkit-background-clip: text;
    background-clip: text;
    color: transparent;
  }
  .subtitle {
    position: absolute;
    top: 587px;
    left: 0;
    right: 0;
    font-family: "Josefin Sans", sans-serif;
    font-weight: 400;
    font-size: 19px;
    line-height: 1.3;
    color: var(--title-white);
  }
  .author {
    position: absolute;
    top: 664px;
    left: 0;
    right: 0;
    font-family: "Josefin Sans", sans-serif;
    font-weight: 700;
    font-size: 24px;
    letter-spacing: 0.1em;
    color: var(--author-teal);
  }
</style>
</head>
<body>
  <main class="stage">
    <article class="cover">
      <div class="cover-art" role="img" aria-label="Mountain landscape at dawn with radiant light rays above the summit, misty teal ridges and small climbers ascending the slopes"></div>
      <div class="cover-text">
        <h1>
          <span class="title-lead">THE QUIET LANTERN</span>
          <span class="title-main">PATH</span>
        </h1>
        <p class="subtitle">A QUIET SEEKER'S JOURNEY<br>TOWARD THE LIGHT AT THE SUMMIT</p>
        <p class="author">ARUN VESH</p>
      </div>
    </article>
  </main>
</body>
</html>
```